Brennock Spa

We are a large Miami Beach spa and salon. I am still building our website but you can use it as a resource to gain a better understanding of who we are ....www.halvorwellness.example.

We offer a comprehensive list of services in hair, nails, massage, skin care, tanning, spray tanning and waxing and we offer high quality products for skin care, tanning and hair. We are open 7 days.

We would like to see a clean and simple menu that looks a lot like the one from "The Spa at Solvara." In particular, we have a copy of a menu from their West Hollywood, CA location that is just beautiful. In the uploaded content you will see a sampling of that menu. We would like to see greys, blacks, silvers, whites and warm colors like reds and oranges. We specifically attempt to remain gender neutral so that we don't attract only girls (with pink colors and flowers etc). The final design should convey a simple, clean, friendly environment and the final product should be sized such that it is 1.) portable and 2.) inexpensive to print. We will be running thousands of these at a time so cost of printing is a consideration.

The booklet consists of two parts: one part is the standard menu with descriptions of services and products and photos etc (think of this as the sales piece that convinces a potential customer to visit) and will be stapled together like you would expect a small menu to be and should resemble the Solvara menu. The prices should not be included in this part of the booklet that will be printed and stapled. The other part is a single insert and is removable and replaceable. I want this removable insert placed in the last page of the book in a folder pocket or something else that you can think of so that when it's time to change prices here that I am not throwing away all of the booklets....I am only replacing the inserts at the end of the menu booklet. Please design this single page insert so that should a customer remove it from the booklet and keep it, that it stands alone with our name, logo, website and phone number. This page can and probably will have to be 2 sided.

At the back of the booklet, I also want the polices to be printed in one page (think fine print in any sort of business dealing.)

With regard to the look and feel slider of economical v upmarket...we definitely want to convey we deliver upmarket services at reasonable prices. Think, world class services and products at reasonable, everyday prices.

With regard to the uploaded files:
I uploaded both EPS and TIF formats. The colors in those files are not the palette we want at all. The colors we want use for the circular logo must match the standard colors as depicted in the uploaded file "Brennocktanrooms"

Target Market(s)

The target market is the average 20-35 year old in Miami Beach that cares about their appearance. The range of clientele is quite diverse.

Industry/Entity Type

Environment

Requirements
Must have
• It must have elegant and simple photographs that relate to the services being offered. We are selling a service set and an environment...so this menu should be reflect that goal. The logo should be repeated often throughout the book but in subtle ways.

Stock photos are fine as long as they don't seem obviously stock.

Should not have
• Nothing buddha like. Nothing themed. It should be all inclusive and not seek to identify with any particular group or gender.

Nothing that fits the stereotype of "Miami Beach." We want to represent ourselves in the same category as the best spas in the world because we moving everything we do in that direction. Think class!

```html
<!DOCTYPE html>
<html lang="en">
<head>
<meta charset="utf-8">
<title>Brennock Spa — Menu Covers</title>
<link rel="stylesheet" href="https://fonts.googleapis.com/css2?family=Cinzel:wght@400&family=Lato:wght@400&display=swap">
<style>
  :root {
    --canvas: #e9e7e4;
    --page-white: #f7f7f6;
    --ink-dark: #2b2b2b;
    --back-black: #121212;
    --back-text: #8d8d8d;
    --ember: #d9541c;
    --logo-light: #f2efe9;
    --rule: #6d6d6d;
  }
  * { box-sizing: border-box; margin: 0; padding: 0; }
  html, body { width: 1200px; height: 512px; overflow: hidden; background: var(--canvas); }
  .spread { position: relative; width: 1200px; height: 512px; }
  .page {
    position: absolute; top: 61px; width: 500px; height: 390px; overflow: hidden;
    box-shadow: 0 4px 14px rgba(0,0,0,0.18);
  }
  .front-cover { left: 70px; background: var(--page-white); }
  .back-cover { left: 630px; background: var(--back-black); }

  .hero-photo {
    position: absolute; left: 0; top: 0; width: 500px; height: 200px;
    background: linear-gradient(100deg, #2a1416 0%, #5a2a26 22%, #3a2a30 45%, #6f7c88 70%, #cfe1ec 88%, #9fb0be 100%);
  }
  .brand-mark {
    position: absolute; left: 22px; top: 14px; width: 110px; text-align: center;
  }
  .brand-mark .mark-dot {
    display: block; width: 22px; height: 22px; border-radius: 50%;
    background: var(--ember); margin: 0 auto 6px;
  }
  .brand-mark .brand-name {
    font-family: 'Cinzel', serif; font-weight: 400; font-size: 15px;
    letter-spacing: 1.5px; color: var(--logo-light); line-height: 1.25;
  }

  .service-strip {
    position: absolute; left: 0; top: 200px; width: 500px; height: 90px;
    display: flex; gap: 2px; background: #fff;
  }
  .service-photo { flex: 1; height: 100%; }
  .service-photo.candle { background: linear-gradient(135deg, #7a1410, #c2361e 55%, #3d0b08); }
  .service-photo.massage-room { background: linear-gradient(160deg, #3b1e4a, #8a5a8e 50%, #e6dde2 80%); }
  .service-photo.salon { background: linear-gradient(180deg, #d8c9b2, #a48a6c 60%, #e8dccb); }
  .service-photo.treatment-room { background: linear-gradient(170deg, #2d1a3a, #6e3e72 55%, #d9cfd6 85%); }
  .service-photo.couples-room { background: linear-gradient(150deg, #3a1f44, #7b4a7f 50%, #cfc3cb 85%); }

  .tagline {
    position: absolute; left: 0; top: 318px; width: 500px; text-align: center;
    font-family: 'Cinzel', serif; color: var(--ink-dark);
  }
  .tagline .tagline-main {
    display: inline-block; font-size: 15px; letter-spacing: 0.6px;
    padding: 0 6px 4px; border-bottom: 1px solid var(--rule);
  }
  .tagline .tagline-sub {
    display: block; font-size: 10px; letter-spacing: 4px; margin-top: 3px;
  }

  .back-cover .brand-mark { left: 195px; top: 16px; }
  .back-cover .mark-dot { width: 18px; height: 18px; }
  .back-cover .brand-name { font-size: 12px; }
  .faint-circle {
    position: absolute; left: 170px; top: 105px; width: 160px; height: 160px;
    border-radius: 50%; background: rgba(255,255,255,0.05);
  }
  .policy-copy {
    position: absolute; left: 32px; top: 84px; width: 436px;
    font-family: 'Lato', sans-serif; font-size: 6.6px; line-height: 1.55;
    color: var(--back-text);
  }
  .policy-copy p { margin-bottom: 12px; }
  .site-address {
    position: absolute; left: 0; bottom: 14px; width: 500px; text-align: center;
    font-family: 'Lato', sans-serif; font-size: 8px; letter-spacing: 2.2px;
    color: var(--back-text);
  }
</style>
</head>
<body>
<main class="spread">
  <section class="page front-cover">
    <div class="hero-photo" role="img" aria-label="Photo of a softly lit tanning room with a bed and a plant"></div>
    <div class="brand-mark">
      <span class="mark-dot"></span>
      <p class="brand-name">BRENNOCK<br>SPA</p>
    </div>
    <div class="service-strip">
      <div class="service-photo candle" role="img" aria-label="Photo of candles glowing in red light"></div>
      <div class="service-photo massage-room" role="img" aria-label="Photo of a massage table with stones in violet light"></div>
      <div class="service-photo salon" role="img" aria-label="Photo of a bright salon with styling chairs"></div>
      <div class="service-photo treatment-room" role="img" aria-label="Photo of a treatment room with a made-up table"></div>
      <div class="service-photo couples-room" role="img" aria-label="Photo of a couples massage room in soft purple light"></div>
    </div>
    <div class="tagline">
      <span class="tagline-main">RELAXING, THERAPEUTIC, SOOTHING</span>
      <span class="tagline-sub">SPA</span>
    </div>
  </section>

  <section class="page back-cover">
    <div class="faint-circle"></div>
    <div class="brand-mark">
      <span class="mark-dot"></span>
      <p class="brand-name">BRENNOCK<br>SPA</p>
    </div>
    <div class="policy-copy">
      <p>Welcome to Brennock Spa, a calm retreat where skilled therapists, fine products and quiet rooms come together to restore balance, ease tension and leave every guest feeling refreshed and renewed.</p>
      <p>Our menu covers hair, nails, massage, skin care, tanning and waxing, each service tailored to your needs and delivered with care by a team that values comfort and detail.</p>
      <p>Every treatment begins with a short consultation so we can understand your goals, suggest the right products and plan a visit that fits your schedule and your budget.</p>
      <p>We are open seven days a week. Arrive a few minutes early, relax in our lounge and let us take care of the rest.</p>
      <p>Gift cards and packages are available at the front desk. Ask our team about seasonal offers and products to continue your routine at home.</p>
    </div>
    <p class="site-address">www.halvorwellness.example</p>
  </section>
</main>
</body>
</html>
```